Laundromat washing machine soap instructions poster

I own a laundromat and need a poster explaining to my customers how to load the soap, bleach and fabric softener into our washing machines. I tried to make a poster on canva but it looks terrible. My Laundromat is called "Suds Harbor" and would like my logo to also be on the poster for branding. I would like the poster to use my blue logo colors to match my brand identity.
Under the photo please include the following text:
" *Please place pods inside the washer"
Thanks
Laundromat

```html
<!DOCTYPE html>
<html lang="en">
<head>
<meta charset="utf-8">
<title>Suds Harbor – Soap Loading Poster</title>
<link href="https://fonts.googleapis.com/css2?family=Bebas+Neue&display=swap" rel="stylesheet">
<style>
  :root {
    --page-bg: #e9e6e1;
    --paper: #ffffff;
    --brand-blue: #2a6fb5;
    --sky-blue: #2f9ad8;
    --deep-blue: #1b63b8;
    --violet: #6a4fc0;
    --foam: #dcefff;
    --rule: #ffffff;
  }
  * { margin: 0; padding: 0; box-sizing: border-box; }
  html, body { width: 1200px; height: 719px; overflow: hidden; }
  body { background: var(--page-bg); position: relative; font-family: "Bebas Neue", sans-serif; }

  .poster {
    position: absolute; left: 345px; top: 19px;
    width: 510px; height: 680px;
    background: var(--paper); overflow: hidden;
    box-shadow: 0 6px 24px rgba(0,0,0,.25);
  }
  .poster-art { position: absolute; inset: 0; }

  .brand { position: absolute; left: 36px; top: 62px; }
  .brand-name {
    display: flex; align-items: center; gap: 8px;
    font-size: 40px; line-height: 1; color: var(--brand-blue); letter-spacing: 1px;
  }
  .brand-dot { width: 14px; height: 14px; border-radius: 50%; background: var(--sky-blue); }
  .brand-tagline {
    margin-top: 4px; margin-left: 22px;
    font-size: 12px; letter-spacing: 2.4px; color: var(--sky-blue);
  }

  .product-photo {
    position: absolute; left: 219px; top: 139px; width: 235px; height: 300px;
    border-radius: 10px;
    background: linear-gradient(180deg, #6b6e73 0%, #5d6065 45%, #d8dadc 60%, #5a5d62 100%);
  }

  .loading-list { position: absolute; left: 32px; top: 0; list-style: none; }
  .loading-item {
    position: absolute; left: 0; display: flex; align-items: center; gap: 12px;
    white-space: nowrap; font-size: 26px; color: var(--paper); letter-spacing: .5px;
  }
  .loading-item.bleach { top: 262px; }
  .loading-item.softener { top: 309px; }
  .loading-item.detergent { top: 355px; }
  .tick-box { width: 15px; height: 15px; }

  .pods-notice {
    position: absolute; left: 0; right: 0; top: 538px;
    text-align: center; color: var(--brand-blue);
    font-size: 61px; line-height: 54px; letter-spacing: .5px;
  }
</style>
</head>
<body>
  <main class="poster">
    <svg class="poster-art" viewBox="0 0 510 680" width="510" height="680" aria-hidden="true">
      <defs>
        <radialGradient id="waterGlow" cx="0.65" cy="0.55" r="0.6">
          <stop offset="0" stop-color="var(--violet)"/>
          <stop offset="0.45" stop-color="var(--deep-blue)"/>
          <stop offset="1" stop-color="var(--sky-blue)"/>
        </radialGradient>
        <linearGradient id="foamFade" x1="0" y1="0" x2="0" y2="1">
          <stop offset="0" stop-color="var(--foam)"/>
          <stop offset="0.55" stop-color="#eef7ff"/>
          <stop offset="1" stop-color="#ffffff"/>
        </linearGradient>
      </defs>
      <path d="M0,159 C120,178 260,125 330,92 C400,60 460,44 510,52 L510,680 L0,680 Z" fill="url(#waterGlow)"/>
      <path d="M0,186 C150,196 280,132 380,104 C440,88 480,90 510,100" fill="none" stroke="#fff" stroke-width="1.5" opacity=".9"/>
      <path d="M0,190 C150,200 280,138 380,110" fill="none" stroke="#8fd0f5" stroke-width="1" opacity=".7"/>
      <path role="img" aria-label="Soap foam and bubbles" d="M0,440 C40,425 70,450 110,432 C150,415 180,445 220,430 C260,412 300,440 340,425 C380,410 420,440 460,422 C480,415 500,420 510,418 L510,680 L0,680 Z" fill="url(#foamFade)"/>
    </svg>

    <div class="brand">
      <div class="brand-name"><span class="brand-dot"></span>Suds Harbor</div>
      <div class="brand-tagline">Laundry and dry cleaning</div>
    </div>

    <div class="product-photo" role="img" aria-label="Photo of the washer's open soap dispenser drawer with its compartments"></div>

    <svg class="poster-art" viewBox="0 0 510 680" width="510" height="680" aria-hidden="true">
      <g fill="none" stroke="var(--rule)" stroke-width="1.5">
        <path d="M21,261 H370 V314"/>
        <path d="M21,308 H299 V325"/>
        <path d="M21,354 H383 V405"/>
        <path d="M290,354 V405"/>
      </g>
      <g fill="var(--rule)">
        <path d="M365,312 L375,312 L370,321 Z"/>
        <path d="M294,323 L304,323 L299,332 Z"/>
        <path d="M378,403 L388,403 L383,412 Z"/>
        <path d="M285,403 L295,403 L290,412 Z"/>
      </g>
    </svg>

    <ul class="loading-list">
      <li class="loading-item bleach">
        <svg class="tick-box" viewBox="0 0 15 15"><rect x="1" y="1" width="13" height="13" rx="2" fill="none" stroke="#fff" stroke-width="1.4"/><path d="M4,7.5 L6.5,10 L11,4" fill="none" stroke="#fff" stroke-width="1.4"/></svg>
        Bleach
      </li>
      <li class="loading-item softener">
        <svg class="tick-box" viewBox="0 0 15 15"><rect x="1" y="1" width="13" height="13" rx="2" fill="none" stroke="#fff" stroke-width="1.4"/><path d="M4,7.5 L6.5,10 L11,4" fill="none" stroke="#fff" stroke-width="1.4"/></svg>
        Fabric&nbsp;&nbsp;Softener
      </li>
      <li class="loading-item detergent">
        <svg class="tick-box" viewBox="0 0 15 15"><rect x="1" y="1" width="13" height="13" rx="2" fill="none" stroke="#fff" stroke-width="1.4"/><path d="M4,7.5 L6.5,10 L11,4" fill="none" stroke="#fff" stroke-width="1.4"/></svg>
        Detergent
      </li>
    </ul>

    <p class="pods-notice">Please place pods<br>inside the washer</p>
  </main>
</body>
</html>
```